BWK Website

We need a website for a company based in Doha Qatar called Crewline Partners Global. It is a global recruitment company, that specializes in both mass recruitment and headhunting. The company is the number 1 one stop shop for recruitment in Qatar. It recruits from all over the world Europe, Asia, Americas, Middle East, Africa for Qatar.
Updates

Target Market(s)

Multinational companies, fortune 500 company CEO's, any top earning companies that are looking for a large number of employees or headhunting employees.
Also for candidates looking for companies to work in Qatar.

Industry/Entity Type

Shop

Colors
ffffff

Requirements
Must have
• Most important qualities the website needs to have:
Clean
Modern
Elegant
Professional
Less Tabs
Minimalisitc

Some examples, I would like you to follow are here:
http://www.velorin.ca/
http://www.trobeckhall.com/
https://quillantro.com/match#

The main color should be white and it has to have a very stylish, modern and cool look. While being minimalistic. I do not want too many tabs. I want it to be simplistic to understand. the only place where the pink logo color is should be in the logo. The logo color should not be anywhere else. It has to be absolutely sleek. Please follow the example websites that I have provided.

I will send the contact details you need to add later. There is no need for a log in page.

Whatever you think that may be important for a recruitment site do suggest. But there is no need for a log in area as we are a different kind of recruitment company.

There should be an area for testimonials from clients. There should also be an area for news flash for the latest countries we are hiring from and the latest companies we are hiring for and the latest positions we are looking for.

Show me the best please. Whoever gives me the best, I will give them an order for the 2nd website too.

Nice to have
• I have included a powerpoint to explain more!

```html
<!DOCTYPE html>
<html lang="en">
<head>
<meta charset="utf-8">
<title>Crewline Partners Global — Global Recruitment</title>
<link rel="stylesheet" href="https://fonts.googleapis.com/css2?family=Zilla+Slab:wght@300;400;600;700&display=swap">
<style>
  :root {
    --page-bg: #fbfbfb;
    --stripe: rgba(0, 0, 0, 0.035);
    --band-bg: #f3f3f3;
    --ink: #333333;
    --ink-soft: #555555;
    --nav-ink: #4a4a4a;
    --brand: #a3245e;
    --white: #ffffff;
    --rule: #e2e2e2;
  }
  * { box-sizing: border-box; margin: 0; padding: 0; }
  html, body {
    width: 1200px;
    height: 900px;
    overflow: hidden;
  }
  body {
    position: relative;
    font-family: "Zilla Slab", Georgia, serif;
    color: var(--ink);
    background-color: var(--page-bg);
    background-image: repeating-linear-gradient(
      -45deg,
      transparent 0,
      transparent 14px,
      var(--stripe) 14px,
      var(--stripe) 15px
    );
  }

  /* Header */
  .site-header {
    position: absolute;
    left: 0; top: 0;
    width: 1200px;
    height: 86px;
    border-bottom: 1px solid var(--rule);
    box-shadow: 0 6px 14px rgba(0, 0, 0, 0.06);
    background-color: rgba(255, 255, 255, 0.6);
  }
  .brand {
    position: absolute;
    left: 113px;
    top: 18px;
    display: flex;
    align-items: center;
    gap: 10px;
    text-decoration: none;
  }
  .brand-dot {
    width: 14px;
    height: 14px;
    border-radius: 50%;
    background: var(--brand);
  }
  .brand-name {
    font-weight: 700;
    font-size: 21px;
    line-height: 22px;
    letter-spacing: 0.5px;
    color: var(--brand);
    text-transform: uppercase;
  }
  .main-nav {
    position: absolute;
    top: 0;
    left: 797px;
    height: 86px;
    display: flex;
  }
  .nav-link {
    position: relative;
    display: block;
    height: 86px;
    line-height: 84px;
    font-size: 19px;
    font-weight: 600;
    color: var(--nav-ink);
    text-decoration: none;
    margin-right: 52px;
  }
  .nav-link.is-active::after {
    content: "";
    position: absolute;
    left: 0; right: 0; bottom: 0;
    height: 6px;
    background: #666666;
  }

  /* Hero */
  .hero {
    position: absolute;
    left: 0; top: 86px;
    width: 1200px;
    height: 415px;
    text-align: center;
  }
  .hero-title {
    margin-top: 88px;
    font-weight: 300;
    font-size: 45px;
    line-height: 59px;
    color: var(--ink-soft);
  }
  .hero-button {
    display: inline-block;
    margin-top: 36px;
    width: 304px;
    height: 63px;
    line-height: 63px;
    border-radius: 12px;
    background: var(--ink);
    color: var(--white);
    font-weight: 300;
    font-size: 32px;
    text-transform: uppercase;
    text-decoration: none;
    letter-spacing: 0.5px;
  }

  /* Services band */
  .services {
    position: absolute;
    left: 0; top: 501px;
    width: 1200px;
    height: 222px;
    background-color: var(--band-bg);
    background-image: repeating-linear-gradient(
      -45deg,
      transparent 0,
      transparent 14px,
      rgba(0, 0, 0, 0.02) 14px,
      rgba(0, 0, 0, 0.02) 15px
    );
  }
  .service-label {
    position: absolute;
    top: 92px;
    font-weight: 700;
    font-size: 32px;
    line-height: 38px;
    color: var(--ink);
    text-transform: uppercase;
    letter-spacing: 0.5px;
  }
  .service-label.is-left { right: 692px; }
  .service-label.is-right { left: 710px; }
  .service-icon {
    position: absolute;
    left: 546px;
    top: 47px;
    width: 128px;
    height: 128px;
  }
</style>
</head>
<body>
  <header class="site-header">
    <a class="brand" href="#">
      <span class="brand-dot"></span>
      <span class="brand-name">Crewline Partners<br>Global</span>
    </a>
    <nav class="main-nav">
      <a class="nav-link is-active" href="#">Home</a>
      <a class="nav-link" href="#">Work</a>
      <a class="nav-link" href="#">Contact</a>
    </nav>
  </header>

  <section class="hero">
    <h1 class="hero-title">Qatar’s leading One-Stop-Shop for<br>Global Recruitment!</h1>
    <a class="hero-button" href="#">Browse Work</a>
  </section>

  <section class="services">
    <h2 class="service-label is-left">Head Hunting</h2>
    <svg class="service-icon" viewBox="0 0 128 128" aria-hidden="true">
      <circle cx="64" cy="64" r="58" fill="none" stroke="#333333" stroke-width="11"/>
      <ellipse cx="64" cy="50" rx="16" ry="19" fill="#333333"/>
      <path d="M30 92 C32 76 44 71 56 68 L64 76 L72 68 C84 71 96 76 98 92 Z" fill="#333333"/>
    </svg>
    <h2 class="service-label is-right">Mass Recruitment</h2>
  </section>
</body>
</html>
```